Creation of a construction/bricklaying business website

Following the template format of "Kestrow 2", the following content would need to be included:
1. Landing page with 3 tiles that go to their own pages.
- Landing page to include background photo and description of services offered.
2. 3 tiles to include:
a) "Contact Us For A Free Quote or Friendly Discussion" Form (middle tile)
b) Case Studies and Testimonials
c) Certifications and Professional Membership
- Design logo to be used from previous ArtQuorum project. Example of logo attached below, please access full JPG files from our account.

Target Market(s)

Prospective clients seeking construction work (bricklaying speciality)

Industry/Entity Type

Residential Construction

Coding

Coded - Design and coding required

Number of Pages Required

4 page

Font styles to use
Sans Serif

Colors

Designer to choose colors to be used in the design.

Requirements
Must have
• Following the template format of "Kestrow 2", the following content would need to be included:
• 1. Landing parent page with 3 tiles that go to the 3 child pages.
• - Landing page to include background photo and description of services offered.
• 2. 3 tiles to include:
• a) "Contact Us For A Free Quote or Friendly Discussion" Form (middle tile)
• b) Case Studies and Testimonials (first tile / left side)
• c) Certifications and Professional Memberships (third tile / right side) (This should include logos of the relevant organisations being displayed. Specifically GLW and the Keel Gate GLW).
• - Design logo to be used from previous ArtQuorum project. Example of logo attached below, please access full JPG files from our account.
Nice to have
• Sleek and modern feel.
• Approachable in terms of how people can contact the company for a quote.
• Traditional pictures to give credibility and comfort around choosing this company.
Should not have
• Cheesy pictures
• Over-complicated
• Simple to use
• Easy URL domain name

```html
<!DOCTYPE html>
<html lang="en">
<head>
<meta charset="utf-8">
<title>R.T.Hale Construction Ltd</title>
<link rel="stylesheet" href="https://fonts.googleapis.com/css2?family=Roboto:wght@400;500;700&display=swap">
<style>
:root{
  --blue:#0b4aa2;
  --blue-dark:#083a80;
  --ink:#1d1d1f;
  --text:#333;
  --muted:#777;
  --field:#f1f0f1;
  --field-line:#c9c9c9;
  --footer:#2b2b2b;
  --page:#ffffff;
}
*{box-sizing:border-box;margin:0;padding:0}
html,body{width:1200px;height:2862px;overflow:hidden;background:var(--page)}
body{position:relative;font-family:"Roboto",Arial,sans-serif;color:var(--text)}
.abs{position:absolute}

/* header */
.brand{left:148px;top:14px;display:flex;align-items:center;gap:10px}
.brand-mark{width:14px;height:14px;background:var(--blue)}
.brand-name{font-size:22px;font-weight:700;color:var(--blue);line-height:1}
.header-phone{left:630px;top:30px;display:flex;align-items:center;gap:12px;font-size:16px;color:var(--ink)}
.btn{display:inline-flex;align-items:center;justify-content:center;background:var(--blue);color:#fff;font-weight:500;border-radius:5px;text-decoration:none}
.btn-quote{left:890px;top:26px;width:150px;height:38px;font-size:15px}

/* hero */
.hero{left:19px;top:80px;width:1169px;height:365px;
  background:linear-gradient(100deg,#4a3a22 0%,#8a6a35 30%,#6b5636 55%,#a88a58 80%,#3d3527 100%)}
.hero-shade{position:absolute;inset:0;background:rgba(0,0,0,.32)}
.hero-copy{position:absolute;left:0;right:0;top:138px;text-align:center;color:#fff}
.hero-title{font-size:32px;font-weight:700;letter-spacing:1px}
.hero-sub{font-size:22px;margin-top:6px}
.btn-ghost{display:inline-flex;margin-top:26px;width:154px;height:38px;align-items:center;justify-content:center;border:1px solid rgba(255,255,255,.8);border-radius:5px;font-size:13px;letter-spacing:1px;color:#fff}
.hero-down{position:absolute;left:575px;top:318px}

/* section headings */
.section-title{left:0;width:1200px;text-align:center;font-size:22px;font-weight:700;color:var(--ink)}
.section-title span{color:var(--blue)}
.section-title i{display:block;margin:6px auto 0;height:3px;background:var(--ink)}

/* services */
.service{width:130px;text-align:center}
.service-photo{width:130px;height:188px}
.service-name{margin-top:20px;font-size:16px;color:var(--ink)}
.service-name.active{color:var(--blue)}

/* about */
.about-copy{left:167px;top:885px;width:366px;font-size:13.5px;line-height:1.4;color:var(--text);text-align:justify}
.about-copy p+p{margin-top:18px}
.btn-about{left:167px;top:1073px;width:134px;height:39px;font-size:13px;border-radius:6px;background:#3a67ad}
.about-photo{left:594px;top:826px;width:443px;height:286px;background:linear-gradient(135deg,#2d4f8a 0%,#6f93c9 40%,#f3d08a 70%,#e9a64c 85%,#375a94 100%)}

/* testimonials */
.review{width:260px;text-align:center}
.avatar{width:104px;height:104px;margin:0 auto;border-radius:50%;border:2px solid #7aa3db;background:#f4e7d6}
.review-name{margin-top:20px;font-size:14px;font-weight:500;letter-spacing:1px;color:var(--ink)}
.review-place{margin-top:5px;font-size:10px;letter-spacing:1px;color:var(--muted)}
.review-text{margin:28px auto 0;width:232px;font-size:13px;line-height:1.5;color:var(--text)}
.slider-nav{left:562px;top:1624px;width:76px;height:49px;background:#e9e9e9;display:flex;align-items:center;justify-content:center;gap:18px}

/* contact */
.lets-talk{left:167px;top:1752px;font-size:22px;font-weight:500;color:var(--ink)}
.lets-talk i,.talk-us i{display:block;margin-top:6px;height:3px}
.lets-talk i{width:130px;background:var(--blue)}
.field{left:167px;width:278px;height:35px;background:var(--field);border:1px dashed var(--field-line);font-size:11px;color:#999;padding:0 14px;display:flex;align-items:center}
.field.area{width:353px;height:88px;align-items:flex-start;padding-top:12px}
.btn-send{left:167px;top:2132px;width:170px;height:46px;font-size:15px;border-radius:6px}
.talk-panel{left:594px;top:1735px;width:445px;height:489px;background:linear-gradient(180deg,#0e3d8c 0%,#1556b0 45%,#0a2f6e 100%);color:#fff}
.talk-us{position:absolute;left:18px;top:20px;font-size:22px;font-weight:500}
.talk-us i{width:130px;background:#fff}
.talk-label{position:absolute;left:18px;font-size:15px;opacity:.9}
.talk-value{position:absolute;left:18px;font-size:21px;font-weight:700}

/* certifications */
.certs{left:184px;top:2268px;width:854px;color:var(--ink)}
.certs h2{font-size:21px;font-weight:500;margin-bottom:12px}
.certs p{font-size:11px;line-height:1.3;margin-bottom:9px}
.certs h3{font-size:17px;font-weight:500;margin:8px 0 14px}
.certs ul{list-style:none}
.certs li{position:relative;padding-left:17px;font-size:11px;line-height:21px}
.certs li::before{content:"";position:absolute;left:0;top:5px;width:4px;height:11px;background:var(--blue)}
.footer{left:19px;top:2804px;width:1169px;height:58px;background:var(--footer);color:#888;font-size:10px;display:flex;align-items:center;justify-content:center}
</style>
</head>
<body>

<header>
  <div class="abs brand"><span class="brand-mark"></span><span class="brand-name">R.T.Hale</span></div>
  <div class="abs header-phone">
    <svg width="20" height="20" viewBox="0 0 24 24" fill="none" stroke="#0b4aa2" stroke-width="1.8"><path d="M5 3h4l2 5-2.5 1.5a11 11 0 0 0 6 6L16 13l5 2v4a2 2 0 0 1-2 2A16 16 0 0 1 3 5a2 2 0 0 1 2-2z"/></svg>
    <span>+012 (4870) 219</span>
  </div>
  <a class="abs btn btn-quote" href="#contact">Request Quote</a>
</header>

<section class="abs hero" role="img" aria-label="Excavator digging soil on a building site">
  <div class="hero-shade"></div>
  <div class="hero-copy">
    <div class="hero-title">IF YOU CAN DREAM IT</div>
    <div class="hero-sub">We can build it!</div>
    <span class="btn-ghost">GET IN TOUCH</span>
  </div>
  <svg class="hero-down" width="20" height="20" viewBox="0 0 20 20" fill="none" stroke="#fff" stroke-width="1.6"><path d="M10 3v10M6 9l4 4 4-4M3 15v2h14v-2"/></svg>
</section>

<h2 class="abs section-title" style="top:478px">OUR <span>SERVICE</span><i style="width:146px"></i></h2>

<div class="abs service" style="left:167px;top:540px"><div class="service-photo" role="img" aria-label="House extension with scaffolding" style="background:linear-gradient(160deg,#b36b4e,#d9c8b4 60%,#6d8ab0)"></div><div class="service-name">Extensions</div></div>
<div class="abs service" style="left:314px;top:540px"><div class="service-photo" role="img" aria-label="Newly built red brick house" style="background:linear-gradient(180deg,#8fbce6 0%,#b5553a 55%,#6f9a4c 100%)"></div><div class="service-name active">New build</div></div>
<div class="abs service" style="left:462px;top:540px"><div class="service-photo" role="img" aria-label="Garden wall with green planting" style="background:linear-gradient(120deg,#b9b9b9 0%,#c9c9c9 45%,#4f8a3a 55%,#2f6a26 100%)"></div><div class="service-name">Garden walls</div></div>
<div class="abs service" style="left:611px;top:540px"><div class="service-photo" role="img" aria-label="Plasterer smoothing a wall with a trowel" style="background:linear-gradient(150deg,#9a9a9a,#e4e4e4 60%,#bdbdbd)"></div><div class="service-name">Plastering</div></div>
<div class="abs service" style="left:761px;top:540px"><div class="service-photo" role="img" aria-label="Bricklayer laying red bricks" style="background:linear-gradient(160deg,#d9d3cc,#b4492c 55%,#7a2f1f)"></div><div class="service-name">Brickwork</div></div>
<div class="abs service" style="left:909px;top:540px"><div class="service-photo" role="img" aria-label="Worker laying paving for groundworks" style="background:linear-gradient(170deg,#4a5b6e,#8a8078 50%,#5f5853)"></div><div class="service-name">Groundworks</div></div>

<div class="abs about-copy">
  <p>We pride ourselves on attention to detail, pride in our completed project and client satisfaction. We believe in full transparency and this is reflected in the jobs we quote for you. We break down each step with both labour and materials cost so you can see exactly what you are paying for.</p>
  <p>Feel free to get in touch and we can talk through what you are looking to achieve.</p>
</div>
<a class="abs btn btn-about" href="#contact">GET IN TOUCH</a>
<div class="abs about-photo" role="img" aria-label="Glass building facade against a sunset sky"></div>

<h2 class="abs section-title" style="top:1168px">What Our <span>Clients</span> Have To Say<i style="width:300px"></i></h2>

<div class="abs review" style="left:175px;top:1269px"><div class="avatar" role="img" aria-label="Client portrait"></div><div class="review-name">DELIA</div><div class="review-place">ASHWELL, KENT</div><p class="review-text">I asked R.T.Hale Construction Ltd to build a wall between the public footpath and my property. This job consisted of using old London stock brick and coping stones on top of the wall.</p></div>
<div class="abs review" style="left:472px;top:1269px"><div class="avatar" role="img" aria-label="Client portrait"></div><div class="review-name">DELIA</div><div class="review-place">ASHWELL, KENT</div><p class="review-text">I asked R.T.Hale Construction Ltd to build a wall between the public footpath and my property. This job consisted of using old London stock brick and coping stones on top of the wall.</p></div>
<div class="abs review" style="left:769px;top:1269px"><div class="avatar" role="img" aria-label="Client portrait"></div><div class="review-name">DELIA</div><div class="review-place">ASHWELL, KENT</div><p class="review-text">I asked R.T.Hale Construction Ltd to build a wall between the public footpath and my property. This job consisted of using old London stock brick and coping stones on top of the wall.</p></div>

<div class="abs slider-nav">
  <svg width="10" height="14" viewBox="0 0 10 14" fill="none" stroke="#222" stroke-width="2"><path d="M8 1L2 7l6 6"/></svg>
  <svg width="10" height="14" viewBox="0 0 10 14" fill="none" stroke="#222" stroke-width="2"><path d="M2 1l6 6-6 6"/></svg>
</div>

<section id="contact">
  <h2 class="abs lets-talk">Let's Talk<i></i></h2>
  <div class="abs field" style="top:1827px">First and Last Name</div>
  <div class="abs field" style="top:1875px">Email Address</div>
  <div class="abs field" style="top:1923px">Contact Phone Number</div>
  <div class="abs field" style="top:1969px">Post Code</div>
  <div class="abs field area" style="top:2013px">Description</div>
  <a class="abs btn btn-send" href="#contact">GET IN TOUCH</a>

  <div class="abs talk-panel" role="img" aria-label="Builders silhouetted on scaffolding at dusk">
    <h2 class="talk-us">Talk To Us<i></i></h2>
    <div class="talk-label" style="top:117px">Call Us</div>
    <div class="talk-value" style="top:140px">100-318-7720</div>
    <div class="talk-label" style="top:197px">Email</div>
    <div class="talk-value" style="top:222px">hello@rthalebuild.co.uk</div>
  </div>
</section>

<section class="abs certs">
  <h2>Certifications and Professional Memberships</h2>
  <p>R.T.Hale Construction is a registered company with the Guild of Local Wallers (GLW). The GLW has a strict membership criteria and dispute resolution service which gives our clients the confidence to entrust their residential building requirements with R.T.Hale Construction.</p>
  <p>To be a member of the GLW, a company must be inspected by GLW inspectors as well as District building inspectors (DBI). GLW and DBI will be present onsite to inspect our work as well as conducting interviews with the owner of R.T.Hale Construction and our employees.</p>
  <p>This membership provides key benefits for our clients. Specifically;</p>
  <p>Being a member of GLW allows R.T.Hale Construction to have district building control (DBC) to approve our work. The GLW has a partnership with the DBC which is the largest building control provider in England and Wales.</p>
  <p>This means that you as the client will have peace of mind knowing that R.T.Hale Construction will have access to expert knowledge on all building regulations - something that other building control providers cannot do at the same level of technical support and knowledge. We hope our clients can feel the guarantee that we will be providing a high profile and quality job for you.</p>
  <p>Once the quote has been verbally agreed between yourself and R.T.Hale Construction LTD, we will send you a contract, using terms and conditions set out by the GLW. R.T.Hale Construction LTD offers a 12 month warranty at no extra charge to you. We do this to provide our clients with a level of comfort knowing that they can contact us should any unforeseen circumstances arise.</p>
  <h3>GLW Membership means that R.T.Hale Construction Ltd:</h3>
  <ul>
    <li>Has a minimum of twelve months trading.</li>
    <li>Have provided a professional reference.</li>
    <li>Have passed credit checks, public record and director checks.</li>
    <li>Verified no un-discharged bankruptcies or relevant and outstanding County Court Judgments.</li>
    <li>Has Public and Employer (if applicable) Liability Insurance.</li>
    <li>Confirmation of business address/details.</li>
    <li>R.T.Hale Construction Ltd has agreed to abide by the GLW Disputes Resolution and Complaints Procedures.</li>
    <li>Has signed up to the GLW Code of Practice.</li>
    <li>Can offer the suite of Sure Build Cover warranty products for the domestic and commercial markets (contact the Sure Build Cover office for rates).</li>
  </ul>
</section>

<footer class="abs footer">© 2018 All rights reserved.</footer>

</body>
</html>
```